Stationery Design Project

We are a packaging machinery manufacturer that mainly serve the food industry.
We now require a full set of stationary including name card, envelop, letter paper, and etc. to match our company image. The logo has been awarded in a previous contest which is attached here.
Updates
Project Deadline Extended
Reason: We have extended the deadline. We have adjusted the deadline before launch to avoid confusion but it turns out the new date wasn't implemented by the system. All designers please feel free to submit your design. Thank you!
Target Market(s)
B2B customer, including decision maker in food factories, chemical factories, etc.
Industry/Entity Type
Industry
Colors
Designer to choose colors to be used in the design.
Look and feel
Each slider illustrates characteristics of the customer's brand and the style your logo design should communicate.

```html
<!DOCTYPE html>
<html lang="en">
<head>
<meta charset="utf-8">
<title>Velnor Stationery Set</title>
<link href="https://fonts.googleapis.com/css2?family=Montserrat:wght@400;600;800&family=Great+Vibes&display=swap" rel="stylesheet">
<style>
  :root {
    --bg: #e3e3e3;
    --paper: #f4f4f4;
    --green: #2f6a36;
    --gray: #7d8187;
    --gray-soft: #e6e6e6;
    --band-soft: #efefef;
    --ink: #555a5f;
    --white: #ffffff;
  }
  * { box-sizing: border-box; margin: 0; padding: 0; }
  html, body { width: 1200px; height: 840px; overflow: hidden; }
  body { background: var(--bg); font-family: "Montserrat", sans-serif; color: var(--ink); }
  .canvas { position: relative; width: 1200px; height: 840px; }

  .piece { position: absolute; background: var(--paper); overflow: hidden; box-shadow: 0 2px 6px rgba(0,0,0,.12); }
  .piece--green { background: var(--green); }

  .corner { position: absolute; top: 0; right: 0; }
  .corner .fill { fill: var(--gray-soft); }
  .corner .band { fill: var(--band-soft); }
  .piece--green .corner .fill { fill: var(--gray); }
  .piece--green .corner .band { fill: #f1f1f1; }

  .brand { position: absolute; display: flex; align-items: center; gap: 6px; font-weight: 800; color: var(--green); letter-spacing: .04em; line-height: 1; }
  .brand__square { background: var(--green); display: block; }
  .piece--green .brand { color: var(--white); }
  .piece--green .brand__square { background: var(--white); }

  .footer { position: absolute; left: 0; right: 0; }
  .footer__green { position: absolute; left: 0; height: 2px; background: var(--green); }
  .footer__gray { position: absolute; right: 0; height: 2px; background: var(--gray); }
  .small { position: absolute; font-size: 5.5px; line-height: 1.5; color: var(--ink); white-space: nowrap; }
  .web { position: absolute; font-size: 5.5px; color: var(--ink); }
  .piece--green .web { color: #dfe9e0; }

  /* Letterhead */
  .letterhead { left: 50px; top: 60px; width: 340px; height: 481px; }
  .letterhead .brand { left: 34px; top: 70px; font-size: 20px; }
  .letterhead .brand__square { width: 14px; height: 14px; }

  /* Folder */
  .folder { left: 420px; top: 60px; width: 340px; height: 481px; }
  .folder .brand { left: 110px; top: 228px; font-size: 24px; }
  .folder .brand__square { width: 17px; height: 17px; }

  /* Envelope */
  .envelope { left: 790px; top: 60px; width: 360px; height: 180px; }
  .envelope .brand { left: 26px; top: 78px; font-size: 18px; }
  .envelope .brand__square { width: 13px; height: 13px; }

  /* Compliment slip */
  .slip { left: 790px; top: 270px; width: 360px; height: 170px; }
  .slip .brand { left: 26px; top: 70px; font-size: 18px; }
  .slip .brand__square { width: 13px; height: 13px; }
  .slip__script { position: absolute; right: 34px; top: 60px; font-family: "Great Vibes", cursive; font-size: 30px; color: var(--ink); }

  /* Business cards */
  .card { width: 250px; height: 160px; top: 600px; }
  .card--front { left: 420px; }
  .card--back { left: 700px; }
  .card--front .brand { left: 18px; top: 50px; font-size: 16px; }
  .card--front .brand__square { width: 11px; height: 11px; }
  .card__person { position: absolute; right: 18px; top: 50px; text-align: right; }
  .card__name { font-size: 8px; font-weight: 600; color: var(--ink); letter-spacing: .04em; }
  .card__role { font-size: 6px; color: var(--ink); margin-top: 2px; }
  .card--back .brand { left: 28px; top: 68px; font-size: 19px; }
  .card--back .brand__square { width: 13px; height: 13px; }
</style>
</head>
<body>
<main class="canvas">

  <!-- Letterhead -->
  <section class="piece letterhead" aria-label="Letterhead">
    <svg class="corner" width="130" height="110" viewBox="0 0 100 100" preserveAspectRatio="none">
      <polygon class="fill" points="30,0 100,0 100,45 55,30"/>
      <polygon class="band" points="10,0 30,0 55,30 100,45 100,62 48,45"/>
    </svg>
    <div class="brand"><span class="brand__square"></span>VELNOR</div>
    <div class="small" style="left:34px; bottom:34px;">Unit 12, Second Floor, Harbor Court, Eastfield 40210<br>T: +44 20 5550 0182 &nbsp; F: +44 20 5550 0183 &nbsp; E: info@velnor.com</div>
    <div class="web" style="right:22px; bottom:34px;">www.velnor.com</div>
    <div class="footer" style="bottom:26px;">
      <div class="footer__green" style="width:72%;"></div>
      <div class="footer__gray" style="width:24%; top:-4px;"></div>
    </div>
  </section>

  <!-- Folder -->
  <section class="piece piece--green folder" aria-label="Presentation folder">
    <svg class="corner" width="200" height="170" viewBox="0 0 100 100" preserveAspectRatio="none">
      <polygon class="fill" points="30,0 100,0 100,45 55,30"/>
      <polygon class="band" points="10,0 30,0 55,30 100,45 100,62 48,45"/>
    </svg>
    <div class="brand"><span class="brand__square"></span>VELNOR</div>
  </section>

  <!-- Envelope -->
  <section class="piece envelope" aria-label="Envelope">
    <svg class="corner" width="120" height="80" viewBox="0 0 100 100" preserveAspectRatio="none">
      <polygon class="fill" points="30,0 100,0 100,45 55,30"/>
      <polygon class="band" points="10,0 30,0 55,30 100,45 100,62 48,45"/>
    </svg>
    <div class="brand"><span class="brand__square"></span>VELNOR</div>
    <div class="small" style="left:26px; bottom:22px;">Unit 12, Second Floor, Harbor Court, Eastfield 40210</div>
    <div class="web" style="right:18px; bottom:42px;">www.velnor.com</div>
    <div class="footer" style="bottom:36px;">
      <div class="footer__green" style="width:72%;"></div>
      <div class="footer__gray" style="width:24%; top:-4px;"></div>
    </div>
  </section>

  <!-- Compliment slip -->
  <section class="piece slip" aria-label="Compliment slip">
    <svg class="corner" width="120" height="76" viewBox="0 0 100 100" preserveAspectRatio="none">
      <polygon class="fill" points="30,0 100,0 100,45 55,30"/>
      <polygon class="band" points="10,0 30,0 55,30 100,45 100,62 48,45"/>
    </svg>
    <div class="brand"><span class="brand__square"></span>VELNOR</div>
    <div class="slip__script">With Compliments</div>
    <div class="small" style="left:26px; bottom:16px;">Unit 12, Second Floor, Harbor Court, Eastfield 40210<br>T: +44 20 5550 0182 &nbsp; E: info@velnor.com</div>
    <div class="footer" style="bottom:40px;">
      <div class="footer__green" style="width:60%;"></div>
      <div class="footer__gray" style="width:36%; top:-4px;"></div>
    </div>
  </section>

  <!-- Business card front -->
  <section class="piece card card--front" aria-label="Business card front">
    <svg class="corner" width="90" height="70" viewBox="0 0 100 100" preserveAspectRatio="none">
      <polygon class="fill" points="30,0 100,0 100,45 55,30"/>
      <polygon class="band" points="10,0 30,0 55,30 100,45 100,62 48,45"/>
    </svg>
    <div class="brand"><span class="brand__square"></span>VELNOR</div>
    <div class="card__person">
      <div class="card__name">MARA LINDQVIST</div>
      <div class="card__role">Managing Director</div>
    </div>
    <div class="small" style="left:18px; bottom:26px;">T: +44 20 5550 0182 &nbsp; F: +44 20 5550 0183<br>M: +44 77 5550 0148 &nbsp; E: info@velnor.com</div>
    <div class="footer" style="bottom:18px;">
      <div class="footer__green" style="width:70%;"></div>
    </div>
    <div class="footer" style="top:78px;">
      <div class="footer__gray" style="width:30%;"></div>
    </div>
  </section>

  <!-- Business card back -->
  <section class="piece piece--green card card--back" aria-label="Business card back">
    <svg class="corner" width="110" height="80" viewBox="0 0 100 100" preserveAspectRatio="none">
      <polygon class="fill" points="30,0 100,0 100,45 55,30"/>
      <polygon class="band" points="10,0 30,0 55,30 100,45 100,62 48,45"/>
    </svg>
    <div class="brand"><span class="brand__square"></span>VELNOR</div>
    <div class="web" style="left:28px; bottom:26px;">www.velnor.com</div>
  </section>

</main>
</body>
</html>
```